Viral food truck (ClipBuzz) needs menu

Our food truck has gone viral on ClipBuzz and we're now requesting a one-page food menu for a taco food truck, please use the logo attached as inspiration and stick to those colors when designing the menu. This is a bilingual menu, please ensure to make the English translation stand out as well.

Size: 8x12 landscape

LOGO - Morales's Taco Bar
318 W Orchard Ln (Entrada/Entrance Brightway Shopping Center)
Maple Hollow, NY 11548
Fri, 6 pm to 11:30 pm | Sat, 1 pm to 11:30 pm | Sun, 1 pm to 11:00 pm

Para horario y información / For pop-up, updated hours and information
Síganos/Follow Us: @moralestacobar

MENU

Tacos.....$4.75 ea
Selección de carne, cilantro, cebolla, salsa roja o verde
Choice of meat, cilantro, onion, red or green salsa

Selección de carne/Choice of Meat
Pollo (Chicken)
Carne Asada (Steak)
Al pastor (Marinated Pork)
Chorizo (Sausage)
Carnitas (Pulled Pork)
Mixta (steak & sausage)........$0.75 extra
Suadero (Brisket).......$0.75 extra
Lengua (Beef Tongue)......$0.75 extra
Tripa (Beef Tripe)......$0.75 extra

Antojitos/Appetizers
Tacos Dorados De Pollo.......$15.00
Taco Dorados De Carne.........$15.00
Quesadilla...........$10.00
Pollo (Chicken) | Carne Asada (Steak) | Queso (Cheese)
Pupusa Revueltas (Chicharone y Queso).........$3.50
Pupusa Queso............$3.50

Especiales / Specials
(#1) 4 Tacos..........$14
(#2) 4 Tacos Dorados/Flautas
Pollo, Creama, Queso Fresco, Aguacate
Chicken, Cream, Queso Fresco, Avocado
*(designer note: need a symbol here) (#3) Chicharones 1lb........$25.00

* Cantidad limitada y temoprada/Limited Quantity/Seasonal

BEBIDAS/BEVERAGES

Horchata.........$6.00

Agua Fresca.......$5.00
SABOR/FLAVOR
Limonada (Lemonade) | Jamaica (Hibiscus) | Sandia (Watermelon) | Piña (Pineapple) | Melon | Mango

Fizzo......$2.00
Zestle.....$2.00
Water.....$1.50
Bubblitos.......$3.00

Target Market(s)

Foodies

Industry/Entity Type

Food truck

Font styles to use
Sans Serif

Colors

Designer to choose colors to be used in the design.

Requirements
Must have
• Color and elements based on our logo, please also visit our Pictagram and Friendbook page for inspiration
Nice to have
• Vintage esthetic

```html
<!DOCTYPE html>
<html lang="es">
<head>
<meta charset="utf-8">
<title>Morales's Taco Bar – Menú / Menu</title>
<link rel="stylesheet" href="https://fonts.googleapis.com/css2?family=Poppins:wght@400;600&family=Alegreya+SC:wght@800&family=Oswald:wght@600&family=Bangers&display=swap">
<style>
  :root{
    --paper:#e9dcc6;
    --paper-dark:#d8c4a4;
    --mustard:#c98f25;
    --mustard-light:#d9a236;
    --brown:#6b3f1e;
    --ink:#2a2624;
    --red:#e02430;
    --red-dark:#b81c26;
    --green:#86ab5d;
    --cream:#fff3dc;
    --yellow:#f4d35e;
    --stage:#ececec;
  }
  *{box-sizing:border-box;margin:0;padding:0}
  html,body{width:900px;height:1200px;overflow:hidden;background:var(--stage)}
  body{position:relative;font-family:"Poppins",sans-serif}
  .menu{
    position:absolute;left:0;top:300px;width:900px;height:600px;overflow:hidden;
    background:radial-gradient(ellipse at 50% 45%,#f1e6d3 0%,var(--paper) 55%,var(--paper-dark) 100%);
  }
  .brand{position:absolute;left:45px;top:28px;width:152px;height:152px;border-radius:50%;
    background:var(--cream);border:4px solid var(--ink);display:flex;align-items:center;justify-content:center;text-align:center}
  .brand__name{font-family:"Oswald",sans-serif;font-weight:600;font-size:22px;line-height:1.1;color:var(--ink);padding:0 14px}
  .dish-photo{position:absolute;left:280px;top:16px;width:271px;height:184px;border:2px solid var(--red);border-radius:28px;
    background:linear-gradient(180deg,#c9cdd0 0%,#b8a37a 45%,#c7883d 70%,#d9c8a3 100%)}
  .info{position:absolute;right:14px;top:22px;display:flex;align-items:center;gap:7px;
    font-family:"Bangers",sans-serif;font-size:18px;letter-spacing:.3px;color:var(--ink);text-transform:uppercase}
  .social{display:flex;align-items:center;gap:3px;font-family:"Poppins",sans-serif;font-weight:600;font-size:9px;letter-spacing:0;text-transform:none}
  .social::before{content:"";width:13px;height:13px;border-radius:50%;background:var(--ink)}
  .brush-head{font-family:"Alegreya SC",serif;font-weight:800;color:var(--mustard-light);background:var(--ink);
    clip-path:polygon(2% 8%,99% 0,100% 70%,97% 100%,0 92%,1% 40%)}
  /* Specials */
  .specials{position:absolute;left:21px;top:232px;width:232px;height:240px;background:var(--mustard);
    clip-path:polygon(2% 0,100% 3%,98% 96%,70% 100%,0 97%,3% 50%);padding:18px 12px 0 12px;color:var(--cream);font-size:10.5px;line-height:1.3}
  .specials__head{position:absolute;left:34px;top:210px;width:222px;height:32px;font-size:17px;padding:4px 0 0 20px;white-space:nowrap}
  .specials p{margin-bottom:8px}
  .specials .num{color:var(--brown);font-weight:600;font-size:12px;white-space:nowrap;letter-spacing:-.2px}
  /* Appetizers */
  .appetizers{position:absolute;left:282px;top:198px;width:267px;height:214px;background:var(--red);padding:8px}
  .appetizers__frame{border:1px dashed var(--cream);height:100%;padding:38px 6px 0 6px}
  .appetizers__head{position:absolute;left:0;top:12px;width:220px;height:30px;font-size:17px;color:var(--yellow);padding:3px 0 0 13px;background:var(--ink)}
  .appetizers li{list-style:none;font-family:"Alegreya SC",serif;font-weight:800;font-size:10.5px;line-height:1.3;color:var(--cream);margin-bottom:7px}
  .appetizers .price{color:var(--yellow);font-family:"Poppins",sans-serif;font-weight:400}
  /* Tacos */
  .tacos{position:absolute;left:576px;top:110px;width:312px;height:312px;background:var(--mustard);
    clip-path:polygon(3% 2%,97% 0,100% 50%,98% 98%,30% 100%,0 96%,2% 45%);padding:36px 10px 0 28px;color:var(--cream);font-size:12px;line-height:1.3}
  .tacos__head{position:absolute;left:650px;top:90px;width:230px;height:34px;background:var(--brown);
    font-family:"Oswald",sans-serif;font-weight:600;font-size:20px;color:var(--cream);text-align:center;padding-top:1px;
    clip-path:polygon(0 10%,100% 0,98% 100%,3% 92%)}
  .tacos__intro{margin-bottom:6px}
  .tacos li{list-style:none;margin-bottom:5px;white-space:nowrap}
  .tacos .extra{font-weight:600}
  /* Beverages */
  .beverages{position:absolute;left:227px;top:410px;width:140px;height:140px;border-radius:50%;background:var(--ink);
    color:var(--cream);text-align:center;padding-top:18px;font-size:11px;line-height:1.25}
  .beverages__head{font-family:"Oswald",sans-serif;font-weight:600;color:var(--mustard-light);font-size:15px;line-height:1.15;margin-bottom:6px}
  .beverages p{margin-bottom:6px}
  .beverages b{font-weight:600}
  /* Flavor */
  .flavor{position:absolute;left:398px;top:436px;width:456px;height:110px;background:var(--green);
    clip-path:polygon(1% 5%,99% 0,100% 60%,98% 100%,2% 97%,0 40%);padding:30px 20px 0 20px;color:var(--cream);font-size:11.5px;line-height:1.45}
  .flavor__head{position:absolute;left:460px;top:422px;width:156px;height:30px;background:var(--brown);
    font-family:"Oswald",sans-serif;font-weight:600;font-size:16px;color:var(--cream);text-align:center;padding-top:2px;
    clip-path:polygon(0 6%,100% 0,97% 100%,2% 94%)}
  .drinks{display:grid;grid-template-columns:1fr 1fr 1fr;margin-top:6px;line-height:1.2}
  .drinks b{font-weight:600;color:var(--yellow)}
  /* Footer */
  .hours{position:absolute;left:0;bottom:0;width:580px;height:46px;background:var(--red-dark);
    font-family:"Bangers",sans-serif;font-size:17px;letter-spacing:.5px;color:var(--cream);padding:12px 0 0 12px;white-space:nowrap;
    clip-path:polygon(0 0,94% 0,100% 100%,0 100%)}
  .address{position:absolute;right:0;bottom:0;width:370px;height:46px;background:var(--ink);
    clip-path:polygon(0 0,100% 0,100% 100%,10% 100%);color:var(--cream);font-size:10px;text-align:center;padding:8px 4px 0 34px;line-height:1.35;white-space:nowrap}
</style>
</head>
<body>
<main class="menu">
  <div class="brand"><span class="brand__name">Morales's Taco Bar</span></div>
  <div class="dish-photo" role="img" aria-label="Photo of three tacos with salsa cups"></div>
  <div class="info">Para horario y información
    <span class="social">Friendbook</span>
    <span class="social">Pictagram</span>
  </div>

  <section class="specials">
    <p><span class="num">(#1) 4 Tacos..........$14</span><br>Selección de carne, cilantro, cebolla, salsa roja o verde<br>Choice of meat, cilantro, onion, red or green salsa</p>
    <p>(#2) 4 Tacos Dorados/Flautas<br>Pollo, Creama, Queso Fresco, Aguacate Chicken, Cream, Queso Fresco, Avocado</p>
    <p><span class="num">(#3) Chicharones 1lb ... $25.00</span><br>* Cantidad limitada y temoprada / Limited Quantity/Seasonal</p>
  </section>
  <h2 class="brush-head specials__head">Especiales / Specials</h2>

  <section class="appetizers">
    <h2 class="brush-head appetizers__head">Antojitos/Appetizers</h2>
    <div class="appetizers__frame">
      <ul>
        <li>Tacos Dorados De Pollo<span class="price">.....$15.00</span></li>
        <li>Taco Dorados De Carne<span class="price">.....$15.00</span></li>
        <li>Quesadilla<span class="price">.......$10.00</span></li>
        <li>Pollo (Chicken) | Carne Asada (Steak) | Queso (Cheese)</li>
        <li>Pupusa Revueltas (Chicharone y Queso)<span class="price">.....$3.50</span></li>
        <li>Pupusa Queso<span class="price">.....$3.50</span></li>
      </ul>
    </div>
  </section>

  <section class="tacos">
    <p class="tacos__intro">Selección de carne, cilantro, cebolla, salsa roja o verde Choice of meat, cilantro, onion, red or green salsa</p>
    <ul>
      <li>Selección de carne/Choice of Meat</li>
      <li>Pollo (Chicken)</li>
      <li>Carne Asada (Steak)</li>
      <li>Al pastor (Marinated Pork)</li>
      <li>Chorizo (Sausage)</li>
      <li>Carnitas (Pulled Pork)</li>
      <li>Mixta (steak &amp; sausage)<span class="extra">........$0.75 extra</span></li>
      <li>Suadero (Brisket)<span class="extra">.......$0.75 extra</span></li>
      <li>Lengua (Beef Tongue)<span class="extra">......$0.75 extra</span></li>
      <li>Tripa (Beef Tripe)<span class="extra">......$0.75 extra</span></li>
    </ul>
  </section>
  <h2 class="tacos__head">Tacos....$4.75 EA</h2>

  <section class="beverages">
    <h2 class="beverages__head">Bebidas /<br>Beverages</h2>
    <p>Horchata.........<br><b>$6.00</b></p>
    <p>Agua Fresca.......<br><b>$5.00</b></p>
  </section>

  <section class="flavor">
    <p>Limonada (Lemonade) | Jamaica (Hibiscus) | Sandia (Watermelon) | Piña (Pineapple) | Melon | Mango</p>
    <div class="drinks">
      <span>Fizzo......<b>$2.00</b><br>Bubblitos.......<b>$3.00</b></span>
      <span>Zestle.....<b>$2.00</b></span>
      <span>Water.....<b>$1.50</b></span>
    </div>
  </section>
  <h2 class="flavor__head">Sabor/Flavor</h2>

  <footer>
    <p class="hours">Fri, 6 PM to 11:30 PM / Sat, 1 PM to 11:30 PM / Sun, 1 PM to 11:00 PM</p>
    <p class="address">318 W Orchard Ln (Entrada/Entrance Brightway Shopping Center)<br>Maple Hollow, NY 11548</p>
  </footer>
</main>
</body>
</html>
```